Vireo M.K. - Diagnostic Ultrasound Flyer

About US
Vireo M.K. is a concierge ultrasound company that provides onsite or offsite diagnostic ultrasounds. We have over 14 years experience in sonography, business management, and customer service. We offer both the physician and patient flexibility, convenience, and access to timely services.

We provide ultrasounds for the following specialties:
Obstetrics/Gynecology
Abdominal
Small Parts
Vascular

Company Features:
1. Onsite or Offsite Scans
2. Images Available Immediately for Referring Physician and Patient
3. Flexible Options for Ultrasound Interpretation/Billing
4. Access to Interpreting Radiologist
5. Final Report Process - 1-2 Business Days/ 1 hour for STAT.
6. PACS Storage with Secure Access.

We need a place to add in our contact information (address, email, website, phone)

We already have a logo and would like to use it ( they are attached). We would the colors to match the logo colors....maybe lighter version of yellow and blue.

```html
<!DOCTYPE html>
<html lang="en">
<head>
<meta charset="utf-8">
<title>Vireo M.K. – Diagnostic Ultrasound Flyer</title>
<link href="https://fonts.googleapis.com/css2?family=Poppins:wght@400;600;700;800&display=swap" rel="stylesheet">
<style>
  :root {
    --blue: #2e3896;
    --navy: #252d7c;
    --yellow: #fbbf3c;
    --yellow-bright: #fcc62a;
    --orange: #f7941d;
    --orange-deep: #f37b2a;
    --white: #ffffff;
    --ink: #111111;
  }
  * { margin: 0; padding: 0; box-sizing: border-box; }
  html, body { width: 849px; height: 1200px; overflow: hidden; background: var(--white); }
  body { font-family: "Poppins", Arial, sans-serif; }
  .flyer { position: relative; width: 849px; height: 1200px; overflow: hidden; background: var(--yellow); }

  .top-stripe { position: absolute; left: 0; top: 0; width: 100%; height: 18px; background: var(--yellow-bright); }
  .header { position: absolute; left: 0; top: 18px; width: 100%; height: 155px; background: var(--white); }
  .brand-name {
    position: absolute; left: 40px; top: 28px;
    font-size: 74px; font-weight: 800; letter-spacing: 2px; line-height: 1;
    color: var(--blue);
  }
  .brand-tagline {
    position: absolute; left: 102px; top: 101px;
    font-size: 23.5px; font-weight: 400; color: var(--ink); letter-spacing: 0.3px;
  }
  .header-photo {
    position: absolute; right: 0; top: 0; width: 230px; height: 155px;
    background: linear-gradient(135deg, #f4f4f4 0%, #d9d9d9 55%, #bdbdbd 100%);
  }

  .hero { position: absolute; left: 0; top: 173px; width: 100%; height: 525px; background: var(--blue); }
  .specialties { position: absolute; left: 28px; top: 30px; list-style: none; color: var(--white); }
  .specialties li { font-size: 80px; line-height: 95px; font-weight: 400; letter-spacing: 0.5px; }
  .specialties li.strong { font-weight: 600; }
  .hero-photo {
    position: absolute; left: 470px; top: 245px; width: 360px; height: 280px;
    background: linear-gradient(90deg, rgba(214,226,240,0.0) 0%, #c9d8ea 25%, #eef2f7 60%, #f6f6f6 100%);
    border-radius: 120px 120px 0 0;
  }
  .experience-badge { position: absolute; left: 577px; top: 107px; width: 205px; height: 205px; }
  .experience-text {
    position: absolute; left: 577px; top: 150px; width: 205px;
    text-align: center; color: var(--white); font-weight: 600; font-size: 19px; line-height: 26px;
  }
  .experience-text strong { font-weight: 800; }

  .divider { position: absolute; left: 35px; top: 693px; width: 778px; height: 15px; border-radius: 8px; background: var(--orange); }

  .features { position: absolute; left: 36px; top: 722px; list-style: none; color: var(--navy); }
  .features li { position: relative; padding-left: 28px; font-size: 27px; line-height: 39px; }
  .features li svg { position: absolute; left: 0; top: 11px; width: 20px; height: 20px; }

  .footer-band { position: absolute; left: 0; top: 1029px; width: 849px; height: 171px; }
  .contact { position: absolute; left: 45px; top: 1052px; list-style: none; color: var(--white); }
  .contact li { position: relative; padding-left: 33px; font-size: 26px; line-height: 39px; }
  .contact li svg { position: absolute; left: 0; top: 9px; width: 22px; height: 22px; }

  .call-label {
    position: absolute; left: 540px; top: 1080px; width: 238px; height: 52px;
    background: var(--white); border-radius: 26px;
    font-size: 22px; font-weight: 700; color: var(--ink);
    padding-left: 38px; line-height: 52px;
  }
  .call-number {
    position: absolute; left: 530px; top: 1130px; width: 263px; height: 44px;
    background: var(--yellow-bright); border-radius: 22px;
    font-size: 28px; font-weight: 700; color: var(--white);
    text-align: left; padding-left: 38px; line-height: 44px; letter-spacing: 0.5px;
  }
  .call-icon {
    position: absolute; left: 490px; top: 1092px; width: 72px; height: 72px;
    border-radius: 50%; background: var(--orange);
  }
  .call-icon svg { position: absolute; left: 18px; top: 16px; width: 38px; height: 40px; }
</style>
</head>
<body>
<div class="flyer">
  <div class="top-stripe"></div>

  <header class="header">
    <div class="brand-name">VIREO M.K.</div>
    <div class="brand-tagline">CONCIERGE ULTRASOUND COMPANY</div>
    <div class="header-photo" role="img" aria-label="Photo of a sonographer performing an ultrasound scan on a patient"></div>
  </header>

  <section class="hero">
    <ul class="specialties">
      <li class="strong">Obstetrics</li>
      <li class="strong">Gynecology</li>
      <li>Abdominal</li>
      <li>Small Parts</li>
      <li>Vascular</li>
    </ul>
    <div class="hero-photo" role="img" aria-label="Photo of a doctor listening with a stethoscope to a pregnant patient"></div>
  </section>

  <svg class="experience-badge" viewBox="0 0 200 200" aria-hidden="true">
    <defs>
      <linearGradient id="badgeFill" x1="0" y1="0" x2="1" y2="0">
        <stop offset="0" stop-color="#f37b2a"/>
        <stop offset="1" stop-color="#fbbf22"/>
      </linearGradient>
    </defs>
    <polygon fill="#fcc62a" points="200,100 180.4,84 192.4,61.7 168.1,54.4 170.7,29.3 145.6,31.9 138.3,7.6 116,19.6 100,0 84,19.6 61.7,7.6 54.4,31.9 29.3,29.3 31.9,54.4 7.6,61.7 19.6,84 0,100 19.6,116 7.6,138.3 31.9,145.6 29.3,170.7 54.4,168.1 61.7,192.4 84,180.4 100,200 116,180.4 138.3,192.4 145.6,168.1 170.7,170.7 168.1,145.6 192.4,138.3 180.4,116"/>
    <circle cx="100" cy="100" r="80" fill="url(#badgeFill)"/>
  </svg>
  <div class="experience-text">WE<br>HAVE OVER<br><strong>14 YEARS</strong><br>EXPERIENCE</div>

  <div class="divider"></div>

  <ul class="features">
    <li><svg viewBox="0 0 20 20"><circle cx="9" cy="10" r="8" fill="none" stroke="#252d7c" stroke-width="1.6"/><path d="M5 10l3.5 3.5L18 3" fill="none" stroke="#252d7c" stroke-width="2.4" stroke-linecap="round"/></svg>Onsite or Offsite Scans</li>
    <li><svg viewBox="0 0 20 20"><circle cx="9" cy="10" r="8" fill="none" stroke="#252d7c" stroke-width="1.6"/><path d="M5 10l3.5 3.5L18 3" fill="none" stroke="#252d7c" stroke-width="2.4" stroke-linecap="round"/></svg>Images Available Immediately<br>for Referring Physician and Patient</li>
    <li><svg viewBox="0 0 20 20"><circle cx="9" cy="10" r="8" fill="none" stroke="#252d7c" stroke-width="1.6"/><path d="M5 10l3.5 3.5L18 3" fill="none" stroke="#252d7c" stroke-width="2.4" stroke-linecap="round"/></svg>Flexible Options for Ultrasound Interpretation/Billing</li>
    <li><svg viewBox="0 0 20 20"><circle cx="9" cy="10" r="8" fill="none" stroke="#252d7c" stroke-width="1.6"/><path d="M5 10l3.5 3.5L18 3" fill="none" stroke="#252d7c" stroke-width="2.4" stroke-linecap="round"/></svg>Access to Interpreting Radiologist</li>
    <li><svg viewBox="0 0 20 20"><circle cx="9" cy="10" r="8" fill="none" stroke="#252d7c" stroke-width="1.6"/><path d="M5 10l3.5 3.5L18 3" fill="none" stroke="#252d7c" stroke-width="2.4" stroke-linecap="round"/></svg>Final Report Process - 1-2 Business Days/ 1 hour for STAT.</li>
    <li><svg viewBox="0 0 20 20"><circle cx="9" cy="10" r="8" fill="none" stroke="#252d7c" stroke-width="1.6"/><path d="M5 10l3.5 3.5L18 3" fill="none" stroke="#252d7c" stroke-width="2.4" stroke-linecap="round"/></svg>PACS Storage with Secure Access.</li>
  </ul>

  <svg class="footer-band" viewBox="0 0 849 171" aria-hidden="true">
    <path d="M0 0 H368 Q398 0 398 30 V39 H849 V171 H0 Z" fill="#2e3896"/>
  </svg>

  <ul class="contact">
    <li><svg viewBox="0 0 22 22"><circle cx="11" cy="11" r="10" fill="none" stroke="#fff" stroke-width="1.5"/><rect x="5.5" y="7.5" width="11" height="7.5" rx="1" fill="none" stroke="#fff" stroke-width="1.4"/><path d="M5.5 8l5.5 4 5.5-4" fill="none" stroke="#fff" stroke-width="1.4"/></svg>vireo.mk@mailbox.com</li>
    <li><svg viewBox="0 0 22 22"><circle cx="11" cy="11" r="10" fill="none" stroke="#fff" stroke-width="1.5"/><circle cx="11" cy="11" r="6.5" fill="none" stroke="#fff" stroke-width="1.3"/><ellipse cx="11" cy="11" rx="3" ry="6.5" fill="none" stroke="#fff" stroke-width="1.3"/><path d="M4.5 11h13" stroke="#fff" stroke-width="1.3"/></svg>www.vireomk.com</li>
    <li><svg viewBox="0 0 22 22"><circle cx="11" cy="11" r="10" fill="none" stroke="#fff" stroke-width="1.5"/><path d="M11 17.5c-3-3.5-4.5-5.8-4.5-7.7a4.5 4.5 0 0 1 9 0c0 1.9-1.5 4.2-4.5 7.7z" fill="none" stroke="#fff" stroke-width="1.4"/><circle cx="11" cy="9.8" r="1.6" fill="none" stroke="#fff" stroke-width="1.3"/></svg>42 Elm Rd, Lakeview City</li>
  </ul>

  <div class="call-label">CALL US NOW!</div>
  <div class="call-number">555-314-2098</div>
  <div class="call-icon">
    <svg viewBox="0 0 38 40" aria-hidden="true"><path d="M8 2c2-1 4 0 5 2l3 7c1 2 0 3-1 4l-2 2c1 4 4 8 8 11l2-2c1-1 3-1 4 0l6 4c2 1 2 3 1 5l-2 3c-2 2-5 2-8 1C13 34 4 24 2 13c-1-3 0-6 2-8z" fill="#fff"/></svg>
  </div>
</div>
</body>
</html>
```